Packaging Graphics Design for TR electronics device

We need a designer to design the graphics that will be printed to the packaging we have designed for our Tenvo Ridge electronics device. Our device is significantly larger but the packacking concept is similar to that of a mobile phone and we envisage the graphics being similar to those used by the main brand. We provide the following additional information:
1. Power point presentation with a more detailed briefing
2. Various renders of our Tenvo Ridge electronics device
3. Packaging design with all components and corresponding dimensions
4. Tenvo Labs logo

```html
<!DOCTYPE html>
<html lang="en">
<head>
<meta charset="utf-8">
<title>Tenvo Ridge Packaging</title>
<link rel="stylesheet" href="https://fonts.googleapis.com/css2?family=Jost:wght@400;600;700&display=swap">
<style>
  :root {
    --backdrop: #edeef6;
    --panel: #f6f6f8;
    --panel-side: #ececf0;
    --edge: #dcdce2;
    --ink: #2b2b2e;
    --device-dark: #1f1f21;
    --device-silver: #c9ccd4;
  }
  html, body {
    margin: 0;
    padding: 0;
    width: 1200px;
    height: 1028px;
    overflow: hidden;
    background: var(--backdrop);
  }
  .canvas {
    position: relative;
    width: 1200px;
    height: 1028px;
    font-family: "Jost", "Helvetica Neue", Arial, sans-serif;
    color: var(--ink);
  }
  .box-side {
    position: absolute;
    left: 150px;
    top: 314px;
    width: 180px;
    height: 400px;
    background: var(--panel-side);
    border: 1px solid var(--edge);
    box-sizing: border-box;
    display: flex;
    align-items: center;
    justify-content: center;
  }
  .brand-mark {
    display: flex;
    align-items: center;
    gap: 10px;
  }
  .brand-mark__square {
    width: 22px;
    height: 22px;
    background: var(--ink);
  }
  .brand-mark__name {
    font-weight: 600;
    font-size: 17px;
    letter-spacing: 2px;
    line-height: 1.05;
    text-transform: uppercase;
  }
  .box-top {
    position: absolute;
    left: 329px;
    top: 314px;
    width: 720px;
    height: 400px;
    background: var(--panel);
    border: 1px solid var(--edge);
    box-sizing: border-box;
  }
  .device-render {
    position: absolute;
    left: 180px;
    top: 56px;
    width: 360px;
    height: 190px;
    border-radius: 34px;
    background: linear-gradient(90deg, var(--device-silver) 0%, var(--device-silver) 22%, var(--device-dark) 24%, #2a2a2d 100%);
  }
  .product-name {
    position: absolute;
    left: 0;
    right: 0;
    top: 300px;
    text-align: center;
    font-size: 38px;
    letter-spacing: 4px;
    text-transform: uppercase;
  }
  .product-name__lead { font-weight: 700; }
  .product-name__tail { font-weight: 400; }
</style>
</head>
<body>
  <main class="canvas">
    <section class="box-side">
      <div class="brand-mark">
        <span class="brand-mark__square"></span>
        <span class="brand-mark__name">Tenvo<br>Labs</span>
      </div>
    </section>
    <section class="box-top">
      <div class="device-render" role="img" aria-label="Product render of the Tenvo Ridge device: black rounded top panel on a silver base"></div>
      <h1 class="product-name"><span class="product-name__lead">Tenvo</span> <span class="product-name__tail">Ridge</span></h1>
    </section>
  </main>
</body>
</html>
```